Patient registration forms

I need 'yes' and 'no' radio buttons added in Acrobat Pro for the two forms and each turned into a PDF. The buttons should line up with each line of inquiry, e.g. "Arthritis"

Radio

```html
<!DOCTYPE html>
<html lang="en">
<head>
<meta charset="utf-8">
<title>Dental History</title>
<link rel="stylesheet" href="https://fonts.googleapis.com/css2?family=Arimo:ital,wght@0,400;0,700;1,700&display=swap">
<style>
:root{
  --ink:#222;
  --muted:#9a9a9a;
  --accent:#f39a2b;
  --rule:#555;
  --paper:#fff;
}
*{box-sizing:border-box;margin:0;padding:0}
html,body{width:849px;height:1200px;overflow:hidden;background:var(--paper)}
body{font-family:"Arimo",Arial,sans-serif;color:var(--ink);font-size:12.5px;position:relative}
.brand{position:absolute;left:34px;top:62px;display:flex;align-items:center;gap:10px}
.brand-dot{width:22px;height:22px;border-radius:50%;background:var(--accent)}
.brand-name{font-size:22px;color:var(--accent);letter-spacing:2px}
.title{font-size:22px;color:var(--muted);letter-spacing:2px;margin-left:8px}
.header-rule{position:absolute;left:0;right:0;top:132px;height:3px;background:var(--accent)}
.line{position:absolute;left:34px;right:62px;display:flex;align-items:flex-end;gap:4px;white-space:nowrap}
.fill{flex:1;border-bottom:1px solid var(--rule);height:12px}
.fill.fixed{flex:none}
.prompt{font-weight:700}
.section-head{position:absolute;left:34px;top:408px;right:0;height:16px;font-weight:700}
.yn{position:absolute;top:0;width:40px;margin-left:-20px;text-align:center;font-style:italic;font-size:14px}
.yn.yes{left:711px}
.yn.no{left:776px}
.q{position:absolute;left:34px;right:0;height:20px;display:flex;align-items:center}
.q .text{width:640px;display:flex;align-items:flex-end;gap:4px;white-space:nowrap}
.q .text .fill{height:11px}
.radio{position:absolute;top:3px;width:14px;height:14px;margin-left:-7px;border:1px solid var(--rule);border-radius:50%;font-style:normal}
.radio.yes{left:711px}
.radio.no{left:776px;border-color:var(--muted);font-size:7px;line-height:12px;text-align:center;color:var(--muted)}
.sig{position:absolute;left:34px;right:62px;display:flex;justify-content:space-between}
.sig div{border-top:1px solid var(--rule);padding-top:4px}
</style>
</head>
<body>
<div class="brand"><span class="brand-dot"></span><span class="brand-name">MERROW</span><span class="title">DENTAL HISTORY</span></div>
<div class="header-rule"></div>

<div class="line" style="top:172px">Name<span class="fill"></span>Nickname<span class="fill"></span>Age<span class="fill fixed" style="width:40px"></span></div>
<div class="line" style="top:194px">Referred By<span class="fill"></span>Previous Dentist<span class="fill"></span></div>
<div class="line" style="top:216px">How long were a patient there?<span class="fill"></span></div>
<div class="line" style="top:236px">Date of Most Recent Dental Exam ____/____/____ Date of Most Recent X-rays ____/____/____</div>
<div class="line" style="top:256px">Date of Most Recent Treatment ____/____/____ Date of Most Recent Cleaning ____/____/____</div>
<div class="line" style="top:276px">How often have you visited your dentist? Not routinely ☐ 3 mos ☐ 6 mos ☐ 12 mos ☐</div>
<div class="line prompt" style="top:314px">What concerns you the most?<span class="fill"></span></div>
<div class="line prompt" style="top:348px">What would you like to change about your smile?<span class="fill"></span></div>

<div class="section-head"><span>PLEASE ANSWER YES OR NO TO THE FOLLOWING QUESTIONS:</span><span class="yn yes">YES</span><span class="yn no">NO</span></div>

<div class="q" style="top:443px"><span class="text">1. Are you fearful of dental treatment?<span class="fill"></span></span><i class="radio yes"></i><i class="radio no">1</i></div>
<div class="q" style="top:464px"><span class="text">2. If so, on a scale of 1 (least) to 10 (most) how fearful are you? [ &nbsp; ]</span><i class="radio yes"></i><i class="radio no">2</i></div>
<div class="q" style="top:485px"><span class="text">3. Have you had an unfavorable dental experience before?<span class="fill"></span></span><i class="radio yes"></i><i class="radio no">3</i></div>
<div class="q" style="top:506px"><span class="text">4. Have you had trouble becoming numb for a dental procedure?<span class="fill"></span></span><i class="radio yes"></i><i class="radio no">4</i></div>
<div class="q" style="top:527px"><span class="text">5. Have you had any braces or other orthodontic treatment?<span class="fill"></span></span><i class="radio yes"></i><i class="radio no">5</i></div>
<div class="q" style="top:548px"><span class="text">6. Have you ever had your bite adjusted?<span class="fill"></span></span><i class="radio yes"></i><i class="radio no">6</i></div>
<div class="q" style="top:569px"><span class="text">7. Are you missing any teeth or have had teeth removed?<span class="fill"></span></span><i class="radio yes"></i><i class="radio no">7</i></div>

<div class="q" style="top:604px"><span class="text">8. Have you whitened or bleached your teeth?<span class="fill"></span></span><i class="radio yes"></i><i class="radio no">8</i></div>
<div class="q" style="top:625px"><span class="text">9. Do you feel uncomfortable about the appearance of your teeth?<span class="fill"></span></span><i class="radio yes"></i><i class="radio no">9</i></div>
<div class="q" style="top:646px"><span class="text">10. Are you disappointed with any previous dental work?<span class="fill"></span></span><i class="radio yes"></i><i class="radio no">10</i></div>

<div class="q" style="top:686px"><span class="text">11. Do you have any problems with your jaw joint?<span class="fill"></span></span><i class="radio yes"></i><i class="radio no">11</i></div>
<div class="q" style="top:707px"><span class="text">12. Do you have any problems chewing gum?<span class="fill"></span></span><i class="radio yes"></i><i class="radio no">12</i></div>
<div class="q" style="top:728px"><span class="text">13. Do you have any problems chewing hard or tough foods?<span class="fill"></span></span><i class="radio yes"></i><i class="radio no">13</i></div>
<div class="q" style="top:749px"><span class="text">14. Have your teeth changed, becoming worn, thinner, or shorter?<span class="fill"></span></span><i class="radio yes"></i><i class="radio no">14</i></div>
<div class="q" style="top:770px"><span class="text">15. Are your teeth becoming crowded or have you noticed spaces?<span class="fill"></span></span><i class="radio yes"></i><i class="radio no">15</i></div>
<div class="q" style="top:791px"><span class="text">16. Is your bite unstable / do you have to squeeze to make your teeth fit?<span class="fill"></span></span><i class="radio yes"></i><i class="radio no">16</i></div>
<div class="q" style="top:812px"><span class="text">17. Do you chew ice, pens, bite your nails, or other habits?<span class="fill"></span></span><i class="radio yes"></i><i class="radio no">17</i></div>
<div class="q" style="top:833px"><span class="text">18. Do you clench your teeth?<span class="fill"></span></span><i class="radio yes"></i><i class="radio no">18</i></div>
<div class="q" style="top:854px"><span class="text">19. Do you wake up with your jaw muscles or your teeth feeling sore?<span class="fill"></span></span><i class="radio yes"></i><i class="radio no">19</i></div>
<div class="q" style="top:875px"><span class="text">20. Have you worn a bite guard or similar appliance?<span class="fill"></span></span><i class="radio yes"></i><i class="radio no">20</i></div>

<div class="q" style="top:915px"><span class="text">21. Have you had any cavities in the past 3 years?<span class="fill"></span></span><i class="radio yes"></i><i class="radio no">21</i></div>
<div class="q" style="top:936px"><span class="text">22. Do you use toothpaste with fluoride?<span class="fill"></span></span><i class="radio yes"></i><i class="radio no">22</i></div>
<div class="q" style="top:957px"><span class="text">23. Do you have any notches in your teeth near the gum line?<span class="fill"></span></span><i class="radio yes"></i><i class="radio no">23</i></div>
<div class="q" style="top:978px"><span class="text">24. Have you ever chipped a tooth or a filling or had a toothache?<span class="fill"></span></span><i class="radio yes"></i><i class="radio no">24</i></div>
<div class="q" style="top:999px"><span class="text">25. Do you get any food caught between any of your teeth?<span class="fill"></span></span><i class="radio yes"></i><i class="radio no">25</i></div>
<div class="q" style="top:1020px"><span class="text">26. Do you have any gum recession?<span class="fill"></span></span><i class="radio yes"></i><i class="radio no">26</i></div>
<div class="q" style="top:1041px"><span class="text">27. Do your gums bleed frequently or bleed when you brush or floss?<span class="fill"></span></span><i class="radio yes"></i><i class="radio no">27</i></div>
<div class="q" style="top:1062px"><span class="text">28. Have you had any teeth become loose?<span class="fill"></span></span><i class="radio yes"></i><i class="radio no">28</i></div>

<div class="sig" style="top:1114px"><div style="width:360px">Patient Signature</div><div style="width:200px">Date</div></div>
<div class="sig" style="top:1160px"><div style="width:360px">Doctor Signature</div><div style="width:200px">Date</div></div>
</body>
</html>
```